Business Card Design Project

Hi,
This is a simple contest. The logo for the back of the card is deigned. See attached files. The front of the card must have :

Directors Name: Tobias
Mob:
e-mail:
Postal Address:
Web Page Adress:

It may also add words: "Leaders in Construction Project Management Services"

Target Market(s)

Business & Home owners alike

Industry/Entity Type

Business

Requirements
Must have
• See details above and logo attached
Should not have
• Images other than logo

```html
<!DOCTYPE html>
<html lang="en">
<head>
<meta charset="utf-8">
<title>Ridgeline Build – Business Card</title>
<link rel="stylesheet" href="https://fonts.googleapis.com/css2?family=Nobile:wght@400;700&family=Arimo:wght@400;700&display=swap">
<style>
  :root {
    --brand-blue: #45c8ff;
    --card-white: #ffffff;
    --ink: #111111;
    --card-edge: #9a9a9a;
  }
  * { margin: 0; padding: 0; box-sizing: border-box; }
  html, body {
    width: 1200px;
    height: 1000px;
    overflow: hidden;
    background: var(--card-white);
  }
  .canvas { position: relative; width: 1200px; height: 1000px; }

  .card-back {
    position: absolute;
    left: 290px; top: 34px;
    width: 653px; height: 462px;
    background: var(--brand-blue);
    display: flex;
    align-items: center;
    justify-content: center;
  }
  .brand-lockup {
    display: flex;
    align-items: center;
    gap: 14px;
    color: var(--card-white);
    font-family: "Arimo", Arial, sans-serif;
    font-weight: 700;
    font-size: 34px;
    letter-spacing: 0.5px;
  }
  .brand-square {
    width: 46px; height: 46px;
    background: var(--card-white);
  }

  .card-front {
    position: absolute;
    left: 290px; top: 516px;
    width: 653px; height: 462px;
  }
  .card-front svg { display: block; }
  .bar { fill: var(--brand-blue); }
  .card-frame { fill: none; stroke: var(--card-edge); stroke-width: 1; }
  .diagonal { stroke: var(--brand-blue); stroke-width: 1; }
  .tagline {
    font-family: "Arimo", Arial, sans-serif;
    font-size: 13.5px;
    fill: var(--brand-blue);
  }
  .director {
    font-family: "Arimo", Arial, sans-serif;
    font-size: 27px;
    fill: var(--ink);
  }
  .contact {
    font-family: "Nobile", Verdana, sans-serif;
    font-size: 15.5px;
    fill: var(--ink);
  }
  .contact .label { font-weight: 700; }
</style>
</head>
<body>
<main class="canvas">
  <section class="card-back">
    <div class="brand-lockup">
      <span class="brand-square"></span>
      <span class="brand-name">RIDGELINE BUILD</span>
    </div>
  </section>

  <section class="card-front">
    <svg width="653" height="462" viewBox="0 0 653 462">
      <g class="bar-chart">
        <rect class="bar" x="0" y="153" width="15" height="309"/>
        <rect class="bar" x="28" y="0" width="68" height="462"/>
        <rect class="bar" x="102" y="224" width="30" height="238"/>
        <rect class="bar" x="147" y="41" width="14" height="421"/>
        <rect class="bar" x="170" y="271" width="61" height="191"/>
        <rect class="bar" x="238" y="392" width="34" height="70"/>
        <rect class="bar" x="280" y="411" width="13" height="51"/>
        <rect class="bar" x="303" y="455" width="206" height="7"/>
      </g>

      <text class="tagline" transform="translate(146 458) rotate(-90)">"Leaders in Construction Project Management Services"</text>

      <line class="diagonal" x1="170" y1="271" x2="653" y2="0"/>
      <text class="director" transform="translate(255 222) rotate(-29.3)">DIRECTOR: Tobias</text>

      <text class="contact" x="305" y="340"><tspan class="label">Mob:</tspan>04123456789</text>
      <text class="contact" x="305" y="364"><tspan class="label">e-mail:</tspan> hello@ridgelinebuild.com</text>
      <text class="contact" x="305" y="388"><tspan class="label">Postal Address:</tspan> PO Box 218, Harbour St,</text>
      <text class="contact" x="305" y="411">Northgate Business Centre,</text>
      <text class="contact" x="305" y="434">Brisbane QLD, 4000</text>
      <text class="contact" x="305" y="454">www.ridgelinebuild.com</text>

      <rect class="card-frame" x="0.5" y="0.5" width="652" height="461"/>
    </svg>
  </section>
</main>
</body>
</html>
```